Business Card Design

Looking for a professional looking business card for a carpentry/construction business that deals with renovations, extensions, homes, and anything carpentry based in Northern Australia. Would like to incorporate the attached logo with backgrounds of white, grey or maybe a close up of timber/wood grain. Thanks

Industry/Entity Type

Carpentry

Contact Information for Business Card

Dean Pollard, Owner, Po Box 2946 Katherine NT 0851, dean-pollard@tallmail.example, 0461907243, Builders Number: 392417CR

Requirements
Should not have
• Power tools/hand tools related to carpentry

```html
<!DOCTYPE html>
<html lang="en">
<head>
<meta charset="utf-8">
<title>Pollard Carpentry – Business Card</title>
<link rel="stylesheet" href="https://fonts.googleapis.com/css2?family=Ubuntu:wght@500&display=swap">
<style>
  :root {
    --timber-light: #e9d3aa;
    --timber-mid: #dcc193;
    --timber-deep: #cfae7d;
    --ink-brown: #5a3414;
    --rule-brown: #6b3a1e;
    --brand-blue: #2f5d8c;
  }
  * { margin: 0; padding: 0; box-sizing: border-box; }
  html, body { width: 1200px; height: 740px; overflow: hidden; background: #ffffff; }
  .card {
    position: relative;
    width: 1200px;
    height: 740px;
    font-family: "Ubuntu", Arial, sans-serif;
    font-weight: 500;
    color: var(--ink-brown);
    overflow: hidden;
  }
  .timber-surface {
    position: absolute; inset: 0;
    background: linear-gradient(100deg, var(--timber-light) 0%, var(--timber-mid) 50%, var(--timber-light) 75%, var(--timber-deep) 100%);
  }
  .brand-name {
    position: absolute;
    left: 76px; top: 180px;
    font-size: 92px;
    line-height: 1;
    color: var(--brand-blue);
    letter-spacing: -1px;
    white-space: nowrap;
  }
  .cut-line {
    position: absolute;
    left: 0; top: 407px;
    width: 976px; height: 6px;
    background: var(--rule-brown);
  }
  .saw-area {
    position: absolute;
    left: 976px; top: 346px;
    width: 152px; height: 76px;
    background: var(--timber-deep);
    opacity: 0.6;
  }
  .postal, .contact-person { position: absolute; white-space: nowrap; }
  .postal { left: 54px; top: 496px; font-size: 32px; line-height: 50px; }
  .postal li { list-style: none; }
  .contact-person { right: 47px; top: 484px; text-align: right; }
  .contact-person .name { font-size: 48px; line-height: 58px; }
  .contact-person .phone { font-size: 42px; line-height: 54px; }
</style>
</head>
<body>
<div class="card">
  <div class="timber-surface" role="img" aria-label="Close-up of light oak timber grain with ruler markings along top and bottom edges"></div>

  <div class="brand-name">Pollard Carpentry</div>

  <div class="cut-line"></div>
  <div class="saw-area" role="img" aria-label="Circular saw blade emblem at the end of the cut line"></div>

  <ul class="postal">
    <li class="address">Po Box 2946 Katherine NT 0851</li>
    <li class="licence">Builders Number: 392417CR</li>
    <li class="email">dean-pollard@tallmail.example</li>
  </ul>

  <div class="contact-person">
    <div class="name">Dean Pollard</div>
    <div class="phone">0461907243</div>
  </div>
</div>
</body>
</html>
```